Sauce business needs a logo design and label design - Re-launching soon

Business based in Chicago, IL. We need a logo design (for Mabel's Sauces) and a label design for our Sauce product line. We make BBQ Sauces, Marinades, Salad dressings, Burger Sauces, Hot sauces, Ketchup, and Mustards
Our products are named under one brand: Mabel's Sauces... Each product will have a different name starting with Mabel's (depending on the flavor of the product). We are looking for a label that will catch consumers eye walking through the store. Our current label doesn't pop enough. We like the colors of Yellow, Red, Orange with a white or black background or any combination thereof.
* Will have to create a label that can be changed to fit particular sauce name and ingredient list, bar codes, etc
Please research designs as we do not want clipart or anything close to any other brands

Target Market(s)

Gourmet foodies, casual consumers,

Industry/Entity Type

Retail

Logo Text

Mabel's Sauces

Requirements
Must have
• Consistent brand scheme that works for all of my Sauce varieties
Should not have
• Clipart or designs/color schemes from other products/brands

```html
<!DOCTYPE html>
<html lang="en">
<head>
<meta charset="utf-8">
<title>Mabel's Sauces — Logo and Label</title>
<link href="https://fonts.googleapis.com/css2?family=Bebas+Neue&display=swap" rel="stylesheet">
<style>
  :root {
    --red: #e8413f;
    --charcoal: #3f3f41;
    --label-grey: #4b4d4e;
    --mint: #9fcfc0;
    --cream: #efe6d6;
    --white: #ffffff;
    --paper: #ffffff;
  }
  * { margin: 0; padding: 0; box-sizing: border-box; }
  html, body { width: 1200px; height: 824px; overflow: hidden; background: var(--paper); }
  .canvas { position: relative; width: 1200px; height: 824px; font-family: "Bebas Neue", sans-serif; }

  .lockup {
    position: absolute; left: 264px; width: 222px; height: 88px;
    display: flex; flex-direction: column; align-items: center; justify-content: center;
    color: var(--white); line-height: 1;
  }
  .lockup--red { top: 216px; background: var(--red); }
  .lockup--dark { top: 358px; background: var(--charcoal); }
  .lockup--plain { top: 528px; color: var(--charcoal); }
  .lockup__name { font-size: 50px; letter-spacing: 1px; }
  .lockup__tag { font-size: 20px; letter-spacing: 4px; margin-top: 2px; }

  .label {
    position: absolute; left: 668px; top: 350px; width: 286px; height: 358px;
    background: var(--label-grey);
  }
  .label__pattern {
    position: absolute; background: var(--mint); opacity: .55;
  }
  .label__pattern--top-left { left: 8px; top: 8px; width: 52px; height: 74px; }
  .label__pattern--top-right { right: 8px; top: 8px; width: 52px; height: 74px; }
  .label__pattern--bottom { left: 8px; top: 254px; width: 270px; height: 84px; }

  .label__brand {
    position: absolute; left: 64px; top: 14px; width: 158px; height: 68px;
    background: var(--red); color: var(--white);
    display: flex; flex-direction: column; align-items: center; justify-content: center; line-height: 1;
  }
  .label__brand-name { font-size: 36px; letter-spacing: 1px; }
  .label__brand-tag { font-size: 15px; letter-spacing: 3px; margin-top: 2px; }

  .label__flavor-lettering {
    position: absolute; left: 24px; top: 106px; width: 238px; height: 60px;
    background: linear-gradient(180deg, #e9e6e1, #cfccc7); opacity: .85; border-radius: 4px;
  }
  .label__chili-art {
    position: absolute; left: 104px; top: 168px; width: 80px; height: 72px;
    background: radial-gradient(circle at 50% 55%, #d8332f, #a9221f); border-radius: 40% 40% 50% 50%;
  }
  .label__ribbon {
    position: absolute; left: 70px; top: 226px; width: 146px; height: 24px;
    background: var(--cream); color: var(--charcoal);
    display: flex; align-items: center; justify-content: center;
    font-size: 15px; letter-spacing: 2px; border: 2px solid var(--charcoal);
  }
  .label__net {
    position: absolute; left: 0; right: 0; top: 342px; text-align: center;
    color: var(--cream); font-size: 10px; letter-spacing: 2px;
  }
</style>
</head>
<body>
<div class="canvas">
  <div class="lockup lockup--red">
    <span class="lockup__name">MABEL'S</span>
    <span class="lockup__tag">SAUCES</span>
  </div>
  <div class="lockup lockup--dark">
    <span class="lockup__name">MABEL'S</span>
    <span class="lockup__tag">SAUCES</span>
  </div>
  <div class="lockup lockup--plain">
    <span class="lockup__name">MABEL'S</span>
    <span class="lockup__tag">SAUCES</span>
  </div>

  <div class="label">
    <div class="label__pattern label__pattern--top-left" role="img" aria-label="Geometric fret pattern in mint, red and cream"></div>
    <div class="label__pattern label__pattern--top-right" role="img" aria-label="Geometric fret pattern in mint, red and cream"></div>
    <div class="label__brand">
      <span class="label__brand-name">MABEL'S</span>
      <span class="label__brand-tag">SAUCES</span>
    </div>
    <div class="label__flavor-lettering" role="img" aria-label="Hand lettered flavor name: Chipotle"></div>
    <div class="label__chili-art" role="img" aria-label="Illustration of two red chili peppers"></div>
    <div class="label__ribbon">ALL NATURAL</div>
    <div class="label__pattern label__pattern--bottom" role="img" aria-label="Band of geometric fret pattern in mint, red and cream"></div>
    <div class="label__net">NET WT 12 OZ (340G)</div>
  </div>
</div>
</body>
</html>
```